Web Design Wecangrowbright

Overview: To develop web site with 1 main page and 1 sample inside page. Site already exists, but has been put offline. Content has been fully rewritten. If I like your style, I will pay extra for additional inside pages.
WHO I AM?
www.wecangrowbright.org was originally created to become an online community for people to use my online tools, researches, and findings to learn how to become happier.
Today, my primary services is “health coaching and lifestyle specialist.” I’m a food specialist suggesting customized solutions for my clients to eat better, how to eat, cook, groceries shop, lose weight, reduce craving, and reverse diseases.
My edge is when a suggest food I explain Why such food hurts them (or make them sick –or reason of diseases) or how the food I suggest can heal them, strengthen them, or make them lose weight. My connection to food is medical and directly impacts my client’s health.
I want to be seen as a professional in clinical nutrition and as a guru in overall wellbeing.
I coach my clients’ lifestyle as a WHOLE, introducing them to new food, fitness, and teaching them techniques to better cope with life. I study their overall health, history, and treatments, diseases, allergies as a WHOLE, connecting all medical specialties.
My services:
I sell coaching sessions, for 1 hour, 2/month for a total program of 6 months. During the sessions, I not only coach client on nutrition, but also on career, relationship, fitness, goals, and the reasons why people can’t achieve their dreams, or how to remove stress or re-organize their lives.
Future services: I may want to sell products such as T-shirts and other promotional items
Payment methods: Since I sell, I’ll need paypal and credit card payment on line. I accept checks as well (they can find my address on “contact us”)
More services, near future:
As a Certified personal fitness Trainer, I will soon offer circuit training (outdoors) and boot camps in the neighborhood to get people moving, at very affordable prices. The goal of those events will be to grow my wecangrowbright community and get new clients for Health coaching.
Knowledgeable about controlling the mind, anger, and stress, I will soon offer group meditations and breathing sessions .
Objectives:
The goal of the site are:
• To entice visitors to become my clients. The look of the site needs to reflect my customized services.
• To offer to spend an hour with client for a free health history.
• To post videos about cooking videos, discussing a theme (sugar craving, which Carbs is good for me?)
• After I meet people and give them my business cards, as they visit my site, they needs to feel impressed by the caliber of expertise.
Schedules and Budget:
Target due date is 1 week from submission of my project. During that phase, I’d like to see a wireframe, colors, styles, incorporating my logo, suggesting pictures. I would like designed tabs, access to videos, and photo library.
Motivations for people to become CLIENTS:
I think what would make people want to get my services is if they see me as an expert in holistic weight loss, someone that they can share their life, thrust, and speak at length without being judged. Visuals are crucial to simply explain effect of food on the body (needs videos main page and archive videos on various topics)
Overall, the emotions we can play with - (key words) feeling energized, feeling strong, in control of your life, a holitistic approach to a new healthy lifestyle, Balance mind, fitness, and diet, take responsibility for your own life, feeling lighter, happier, more peaceful.
Key issues of my clients:
Weight issues, high blood pressure, depression, anxiety, stress, don’t know and what to cook, suffer from diabetes, celiac, digestive diseases. People are fatigued or can’t sleep. They are addicted to sugar, coffee, fast food, speedy life.
Another issue is finding time to eat better, making exercise a routine, making the time to remove stress and enjoy life.
How do I solve clients’ problems?:
Rather than being treated by various medical specialists, I look over their Overall health since childhood. I try to find triggers of their sicknesses that often originate from their lifestyle (stress, lack of exercise, eating junk, allergies) and I recommend life modification, introduce new food, exercise , and help them shuffle their lives around. My approach is extremely customized and always requires Hours of research on my side to fully guide a client.
Demographics:
Teenagers, singles, families, young mothers. Most of clients come with weight issues, some may come to reduce cravings.
Key Messages:
The main page (please find attached “wireframe”) shall give the visitor a sense he found the guru in holistic health. Whatever medical concern they have or struggle will finally be taken care of. Someone loves them and truly cares. Food knowledge is medical, flavor, and based on client’s own taste and willingness to try. The overall feel needs to be sleek and professional.
Call to Action
Ideally, I want people to e-mail me their filled up health history (can download blank men or women health history form) so I can schedule an appointment with them (the best solution for me)
People can also call me. Since calling me is for general questions about my program, I would prefer the e-mail version whereby clients send me their health history.
Creative Considerations
Layout – considerations in accordance to brand guidelines
Need suggetions!
Tone –
Expert in clinical food and holistic health.
Visual
Color palette : I’m not sure, but the background could be light gray (clinical health), golden desert, sahara desert, earthy, pottery (well being) warm colors (orange to warm brown) or other suggestion?
Photography: I thought about flash picture. 1 picture as banner with a message on it. About 3 pictures rotate randomly.
Picture A: is “holistic food, green vegetables, natural edible roots, or cruciferous vegetables, a platter of fresh fruits and vegies, or fresh market (spices, roots, fruits and vegies). Picture needs to be crisp clear.
Picture B: Ideally: a lady fitness trainer training group exercise outdoors, in a park, or a group of people exercising outside, people look happy, boot camp training, circuit training as a group
Picture C: a picture representing the soul ,meditation, a person relaxing next to beach or in forest, next to flowers or lushy plants, a person re-energizing.
Logo: attached as separate files with various backgrounds
Icons: may look cool to use vegies or weight, happy face, or ginger root…
typography, graphics: need suggestions!

Resources
• I have an existing website name “wecangrowbright.org” the site has been put out of internet since we were trying to change it. Let me know if you need to access site. Content of the site is ineffective.
• All content has been written. You can suggest layouts and tabs
Updates

Target Market(s)

My industry is Health care, holistic Health (no medications, no supplements, no surgeries)
Buyer’s Type could be anyone wanting to lose weight, feel better, reduce stress, learn to eat, to cook, to groceries shop. My buyers are confused about all diets.My audience is people WHO WANT change in their lives. Some people know they should eat better, they mostly need support and motivation.
Typical buyer is someone who wants a new chance, a new life!
My primary target buyer is:
1. Family. I wish to coach the entire family into healthier eating and teach them how to cook and eat as a family by changing their habits.
My secondary markets are:
1.Teenagers (often eating emotionally and confused about diets)

Industry/Entity Type

Requirements
Must have
• • Format – web, print, video, sound
I would like videos (youtube connect) – facebook connect – calendar (I will update) – I will update my content, videos, and photo library regularly – people should be able to e-mail me from site – maybe be able to go through web conference. 2 different words or pdf forms shall be available for download or online filling, then they should be able to e-mail forms through site or through their personal mail system. They can also print and mail it to me.
Managing the site:
I would like to upload videos, pictures and text freely and easily. I would like to manage and update content
Nice to have
• would look cool to use entire background as a super picture!

```html
<!DOCTYPE html>
<html lang="en">
<head>
<meta charset="utf-8">
<title>Wecangrowbright – Balanced Nutrition, Mind, and Fitness</title>
<link href="https://fonts.googleapis.com/css2?family=Arimo:wght@400;700&family=Marcellus&display=swap" rel="stylesheet">
<style>
:root{
  --bar:#3a3b3d;
  --bar-dark:#2b2c2e;
  --green:#7cb82f;
  --green-dark:#3f8a1c;
  --orange:#f7941d;
  --orange-light:#ffb83a;
  --orange-deep:#e86a0c;
  --page:#ececec;
  --panel:#e2e2e2;
  --panel-border:#cfcfcf;
  --text:#3b3b3b;
  --muted:#6b6b6b;
  --white:#ffffff;
  --blue:#1e6fc8;
  --bubble:#9c9c9c;
}
*{box-sizing:border-box;margin:0;padding:0}
html,body{width:775px;height:1200px;overflow:hidden}
body{position:relative;background:var(--page);font-family:"Arimo",Arial,sans-serif;color:var(--text)}
.abs{position:absolute}

/* top bar */
.topbar{left:0;top:0;width:775px;height:34px;background:linear-gradient(var(--bar),var(--bar-dark))}
.tagline{left:10px;top:9px;font-size:13px;color:var(--green)}
.hh-button{left:180px;top:6px;height:21px;padding:0 12px;border-radius:11px;background:#55565a;border:1px solid #777;color:#f2c230;font-size:10px;line-height:19px}
.account{top:11px;font-size:11px;font-weight:700;color:var(--green)}
.search{left:556px;top:5px;width:202px;height:24px;border-radius:12px;background:linear-gradient(#fff,#ddd);font-size:11px;color:#777;padding:5px 12px}

/* header */
.header{left:0;top:34px;width:775px;height:130px;background:radial-gradient(ellipse at 50% 20%,#fffbea 0,#f4f1e8 40%,var(--page) 75%)}
.brand-dot{left:140px;top:44px;width:58px;height:58px;border-radius:50%;background:var(--green)}
.brand-name{left:210px;top:44px;font-size:34px;color:var(--green-dark);font-family:"Arimo",Arial,sans-serif;font-weight:700}
.brand-sub{left:212px;top:85px;font-size:10.5px;font-weight:700;letter-spacing:.8px;color:var(--green-dark)}

/* nav */
.nav{left:0;top:124px;width:775px;height:26px;display:flex;align-items:center;font-size:12px;font-weight:700;color:#333}
.nav span{padding:0 14px}
.nav .sep{color:#aaa;font-weight:400;padding:0 6px}
.nav .active{background:linear-gradient(var(--orange-light),var(--orange-deep));color:#fff;border-radius:13px;padding:6px 14px;border:2px solid #fff;box-shadow:0 0 0 1px #d9d9d9}

/* hero */
.hero-frame{left:10px;top:164px;width:748px;height:365px;background:#fff;border:1px solid var(--panel-border)}
.hero-photo{left:18px;top:172px;width:732px;height:349px;background:linear-gradient(180deg,#c3d87a 0,#7fa73a 45%,#5c7e2e 100%)}
.hero-video{left:490px;top:240px;width:228px;height:194px;background:#4a4a44;border:2px solid #6a6a62;padding:8px}
.hero-video .inner{width:100%;height:100%;background:linear-gradient(#c8c4be,#8a857d)}
.play{width:46px;height:46px;border-radius:50%;background:var(--orange-deep);border:3px solid #fff}
.hero-caption{left:18px;top:448px;width:732px;height:73px;background:linear-gradient(90deg,rgba(40,70,30,.75),rgba(40,70,30,.35))}
.hero-title{left:36px;top:462px;font-size:50px;font-weight:700;color:var(--orange);letter-spacing:1px}
.hero-title small{font-size:30px;color:#fff;letter-spacing:0}
.arrow{top:336px;width:18px;height:26px;background:#fff;border:1px solid #ccc;font-size:10px;line-height:24px;text-align:center;color:#555}

/* orange band */
.band{left:0;top:490px;width:775px;height:210px;background:linear-gradient(var(--orange-light) 0,var(--orange) 30%,var(--orange-deep) 45%,var(--page) 100%)}
.col-title{top:558px;font-family:"Marcellus",Georgia,serif;font-size:18px;color:#fff}
.panel{background:var(--panel);border:1px solid var(--panel-border);border-radius:3px}

.thumb{left:14px;width:182px;height:104px;border:2px solid #fff}
.thumb-a{top:590px;background:linear-gradient(#d9a23a,#8a2c12)}
.thumb-b{top:700px;background:linear-gradient(#b7c7d3,#6a8aa0 70%,#3d5260)}

.welcome-text{left:228px;top:592px;width:280px;font-size:9.4px;line-height:14px;color:#555}
.welcome-art{left:400px;top:592px;width:110px;height:110px;border-radius:50%;background:radial-gradient(#f2e4c8,#d98a3a 70%,#fff 72%)}
.cta{left:226px;top:787px;height:15px;padding:0 8px;background:var(--orange);border:1px solid #c65f08;color:#222;font-size:9.5px;font-weight:700;line-height:13px}

.bubble{left:548px;width:202px;background:var(--bubble);border-radius:3px;padding:8px 10px;color:#fff;font-size:9.4px;line-height:14px}
.bubble b{display:block;font-size:10px;margin-bottom:6px}
.bubble-tail{left:562px;width:0;height:0;border-left:12px solid var(--bubble);border-bottom:14px solid transparent}
.quote-name{left:576px;font-size:10px;font-weight:700;color:#444}
.readmore{left:682px;top:787px;height:15px;padding:0 6px;background:var(--orange);border:1px solid #c65f08;font-size:9.5px;font-weight:700;line-height:13px}

/* login */
.login-strip{left:10px;top:828px;width:748px;height:126px}
.login-box{left:18px;top:836px;width:478px;height:108px;background:#fff;border:1px solid #ddd}
.login-head{left:18px;top:836px;width:478px;height:24px;background:linear-gradient(#6ec133,#2d8b17);font-family:"Marcellus",Georgia,serif;font-size:16px;color:#fff;padding:3px 8px}
.field{left:28px;width:202px;height:22px;background:linear-gradient(#e6e6e6,#d5d5d5);border:1px solid #ccc;font-size:10px;font-weight:700;color:#444;padding:5px 8px}
.submit{left:112px;top:925px;width:58px;height:16px;background:#fff;border:1px solid #ccc;border-bottom:none;font-size:10px;font-weight:700;color:var(--green-dark);text-align:center;line-height:15px}
.login-note{left:242px;top:868px;width:246px;font-size:9.6px;line-height:13.5px;color:#555}
.subscribe-art{left:536px;top:830px;width:210px;height:66px;background:linear-gradient(90deg,#e8d5c2,#f7f7f7)}
.subscribe{left:514px;top:890px;width:224px;height:52px;background:linear-gradient(#4aa3ef,#1556b0);border-radius:8px;padding:6px 8px}
.subscribe .label{color:#fff;font-size:11px}
.subscribe .input{position:absolute;left:8px;top:26px;width:150px;height:18px;background:#fff;border:1px solid #0d3e85;font-size:9.5px;font-weight:700;color:#333;padding:2px 6px}
.subscribe .go{position:absolute;left:164px;top:25px;width:50px;height:20px;background:linear-gradient(#e9f2fc,#9dbfe8);color:var(--blue);font-weight:700;font-size:11px;text-align:center;line-height:20px;border:1px solid #0d3e85}

/* feature icons */
.features{left:10px;top:970px;width:748px;height:136px;background:linear-gradient(var(--orange-light),var(--orange) 60%,var(--orange-deep));border-radius:3px}
.feature{top:978px;width:130px;text-align:center;color:#fff;font-family:"Marcellus",Georgia,serif;font-size:14.5px;line-height:16px}
.feature .ring{width:86px;height:86px;margin:0 auto 8px;border-radius:50%;background:#8a5a12;padding:7px}
.feature .ring div{width:100%;height:100%;border-radius:50%;background:radial-gradient(#fff,#e7e1d8)}

/* footer */
.footer{left:0;top:1126px;width:775px;height:74px;background:linear-gradient(var(--bar),var(--bar-dark))}
.phone{left:40px;top:1138px;font-size:21px;color:var(--orange-light)}
.email{left:40px;top:1177px;font-size:12px;font-weight:700;color:#e6e6e6}
.copy{left:256px;top:1160px;font-size:9.6px;color:#ddd}
.social{top:1146px;width:38px;height:38px;border-radius:50%;background:radial-gradient(circle at 40% 35%,#6fa6e6,#1d4f93 70%);border:2px solid #9bb7d8}
</style>
</head>
<body>

<div class="abs topbar"></div>
<div class="abs tagline">The fastest way get a new life</div>
<div class="abs hh-button">Full up HH form</div>
<div class="abs account" style="left:452px">Login</div>
<div class="abs account" style="left:498px">Register</div>
<div class="abs search">Search...
  <svg style="position:absolute;right:10px;top:5px" width="13" height="13" viewBox="0 0 13 13"><circle cx="5" cy="5" r="4" fill="none" stroke="#666" stroke-width="1.6"/><line x1="8" y1="8" x2="12" y2="12" stroke="#666" stroke-width="2"/></svg>
</div>

<div class="abs header"></div>
<div class="abs brand-dot"></div>
<div class="abs brand-name">Wecangrowbright</div>
<div class="abs brand-sub">BALANCED NUTRITION, MIND, AND FITNESS</div>

<nav class="abs nav" style="left:24px;width:740px">
  <span>Home</span><span class="sep">/</span>
  <span class="active">Your coaching program</span><span class="sep">/</span>
  <span>Why a health coach</span><span class="sep">/</span>
  <span>About your coach</span><span class="sep">/</span>
  <span>Recipe</span><span class="sep">/</span>
  <span>Body &amp; Mind workouts</span>
</nav>

<div class="abs band"></div>

<div class="abs hero-frame"></div>
<div class="abs hero-photo" role="img" aria-label="Photo of a happy family riding bicycles together in a sunny green park"></div>
<div class="abs hero-video">
  <div class="inner" role="img" aria-label="Video still of a woman stretching backwards over a green exercise ball"></div>
  <div class="abs play" style="left:94px;top:72px"><svg width="40" height="40" viewBox="0 0 40 40"><polygon points="15,11 29,20 15,29" fill="#fff"/></svg></div>
</div>
<div class="abs hero-caption"></div>
<div class="abs hero-title">ENJOY <small>LIFE TO THE FULLEST</small></div>
<div class="abs arrow" style="left:10px">&#9664;</div>
<div class="abs arrow" style="left:740px">&#9654;</div>

<div class="abs col-title" style="left:16px">Health Video</div>
<div class="abs col-title" style="left:224px">Welcome <span style="color:#222">Wecangrowbright</span></div>
<div class="abs col-title" style="left:548px">Testimonials</div>

<div class="abs panel" style="left:10px;top:586px;width:190px;height:226px"></div>
<div class="abs thumb thumb-a" role="img" aria-label="Video still of a colourful pile of fresh fruits and vegetables"></div>
<div class="abs play" style="left:78px;top:618px"><svg width="40" height="40" viewBox="0 0 40 40"><polygon points="15,11 29,20 15,29" fill="#fff"/></svg></div>
<div class="abs thumb thumb-b" role="img" aria-label="Video still of a woman leaping on a beach at sunset"></div>
<div class="abs play" style="left:78px;top:728px"><svg width="40" height="40" viewBox="0 0 40 40"><polygon points="15,11 29,20 15,29" fill="#fff"/></svg></div>

<div class="abs panel" style="left:216px;top:586px;width:308px;height:226px"></div>
<div class="abs welcome-art" role="img" aria-label="Circular collage of a healthy meal, a family and fitness scenes"></div>
<div class="abs welcome-text">
  <p style="width:172px">Lorem Ipsum available, but the majority have suffered alteration in some form, by injected humour, or randomised words which don't look even slightly believable. If you are going to use a passage of Lorem Ipsum, you need to be sure there isn't anything embarrassing hidden Lorem Ipsum, Lorem Ipsum Lorem Ipsum.</p>
  <p>Lorem Ipsum available, but the majority have suffered alteration in some form, by injected humour, or randomised words which don't look even slightly believable. If you are going to use a passage of Lorem Ipsum, you need to be sure there isn't anything embarrassing.</p>
</div>
<div class="abs cta">Contact Your Health Coach &#9656;</div>

<div class="abs panel" style="left:542px;top:586px;width:216px;height:226px"></div>
<div class="abs bubble" style="top:592px;height:92px"><b>18 Aug, 2012</b>Lorem Ipsum available, but the majority have suffered alteration in some form, by injected humour, or randomised words which don't look even slightly believable.</div>
<div class="abs bubble-tail" style="top:684px"></div>
<div class="abs quote-name" style="top:687px">Lorem Ipsum</div>
<div class="abs bubble" style="top:706px;height:66px"><b>18 Aug, 2012</b>Lorem Ipsum available, but the majority have suffered alteration in some form,</div>
<div class="abs bubble-tail" style="top:772px"></div>
<div class="abs quote-name" style="top:778px">Lorem Ipsum</div>
<div class="abs readmore">Read More &#9656;</div>

<div class="abs panel login-strip"></div>
<div class="abs login-box"></div>
<div class="abs login-head">Client Login</div>
<div class="abs field" style="top:870px">Username</div>
<div class="abs field" style="top:898px">Password</div>
<div class="abs submit">SUBMIT</div>
<div class="abs login-note">Get Your free login to access to monthly newsletter and archived articles (anyone) as awell as teleconferences to access videos, that privilege is for clients only (please sbmit your e-mail address and client Number) - thanks!</div>
<div class="abs subscribe-art" role="img" aria-label="Photo of a woman relaxing with a laptop beside paper envelopes"></div>
<div class="abs subscribe">
  <div class="label">subscribe to email</div>
  <div class="input">email@domin.com</div>
  <div class="go">Submit</div>
</div>

<div class="abs features"></div>
<div class="abs feature" style="left:16px"><div class="ring"><div role="img" aria-label="Illustration of a ring of people holding hands"></div></div>Wecangrowbright community</div>
<div class="abs feature" style="left:169px"><div class="ring"><div role="img" aria-label="Illustration of an envelope with an email symbol"></div></div>Newsletter</div>
<div class="abs feature" style="left:314px"><div class="ring"><div role="img" aria-label="Illustration of a wall calendar with a photo"></div></div>Calender</div>
<div class="abs feature" style="left:467px"><div class="ring"><div role="img" aria-label="Illustration of an orange feed symbol"></div></div>Blog</div>
<div class="abs feature" style="left:622px"><div class="ring"><div role="img" aria-label="Illustration of a printed form document"></div></div>Health History Forms</div>

<footer class="abs footer"></footer>
<svg class="abs" style="left:10px;top:1138px" width="20" height="28" viewBox="0 0 20 28"><rect x="2" y="1" width="16" height="26" rx="3" fill="#1b5fae" stroke="#8fb6e4"/><rect x="5" y="5" width="10" height="15" fill="#cfe2f7"/><circle cx="10" cy="23.5" r="1.6" fill="#cfe2f7"/></svg>
<div class="abs phone">555.214.7730</div>
<svg class="abs" style="left:10px;top:1176px" width="22" height="16" viewBox="0 0 22 16"><rect x="1" y="1" width="20" height="14" fill="#6cb33f"/><polyline points="1,1 11,9 21,1" fill="none" stroke="#fff" stroke-width="1.5"/></svg>
<div class="abs email">hello@wecangrowbright.org</div>
<div class="abs copy">Copyright © 2012, Wecangrowbright.org. All Rights Reserved</div>
<div class="abs social" style="left:580px"></div>
<div class="abs social" style="left:625px"></div>
<div class="abs social" style="left:670px"></div>
<div class="abs social" style="left:718px"></div>

</body>
</html>
```